New Podcast focussing on non-mainstream interventions for guidance needs podcast art

I need an exquisite piece of podcast art work for the launch of my new podcast 'Beyond the Still'. This podcast explores unorthodox, esoteric and unconventional methods to find peace, clarity and direction in life. Topics include family Constellations Systems, Psychedelics, Equine Therapy and Floatation to name a few. A teaser has been posted on Talvora with a strong response. The audience is primarily midlifers or those in a career/personal crisis of direction. It's meant to comfort, inform and empower and offer other ways rather than mainstream to work out what to do with your life. The file shared with you shows the pic used on Talvora as it's illustrating the idea of illumination. You can use it or not, and whilst I am ex-Military, I don't want the cover to convey an overly military influence. I'd like 'Beyond the Still' to feature on the art work and my name, Mirela Dunford. I'd like inspiration, creativity, and the idea of hope conveyed as well as clarity and courage. Whilst the podcast is about finding your direction please do no use compass images or cross road images as that is too obvious.
Hope that all helps. Looking forward to your ideas.

```html
<!DOCTYPE html>
<html lang="en">
<head>
<meta charset="utf-8">
<title>Beyond the Still — Podcast Cover</title>
<link rel="stylesheet" href="https://fonts.googleapis.com/css2?family=Raleway:wght@300&family=Saira+Stencil+One&display=swap">
<style>
  :root {
    --sky-top: #8c8791;
    --sky-rose: #c98a78;
    --sky-peach: #eea862;
    --sun-gold: #ffd45a;
    --sun-core: #fff1b0;
    --field-amber: #b8662c;
    --field-dark: #2c1a14;
    --title-cream: #fff4cf;
    --label-white: #ffffff;
  }
  * { margin: 0; padding: 0; box-sizing: border-box; }
  html, body {
    width: 1200px;
    height: 1200px;
    overflow: hidden;
    background: var(--field-dark);
  }
  .cover {
    position: relative;
    width: 1200px;
    height: 1200px;
    overflow: hidden;
  }
  .cover__scene {
    position: absolute;
    inset: 0;
    width: 1200px;
    height: 1200px;
    display: block;
  }
  .cover__title {
    position: absolute;
    inset: 0;
    width: 1200px;
    height: 1200px;
    display: block;
  }
  .cover__title text {
    font-family: "Saira Stencil One", "Black Ops One", sans-serif;
    fill: var(--title-cream);
    fill-opacity: 0.86;
  }
  .cover__label {
    position: absolute;
    left: 0;
    width: 1200px;
    text-align: center;
    font-family: "Raleway", "Helvetica Neue", sans-serif;
    font-weight: 300;
    color: var(--label-white);
    line-height: 1;
    white-space: nowrap;
  }
  .cover__kicker {
    top: 98px;
    font-size: 64px;
    letter-spacing: 0.32em;
    padding-left: 0.32em;
  }
  .cover__host {
    top: 1054px;
    font-size: 64px;
    letter-spacing: 0.36em;
    padding-left: 0.36em;
  }
</style>
</head>
<body>
  <main class="cover">
    <svg class="cover__scene" viewBox="0 0 1200 1200" role="img"
         aria-label="Illustration: a lone walker with a backpack crossing a grassy plain at sunrise, a tree silhouette on the left and distant hills under a glowing golden sky">
      <defs>
        <linearGradient id="sky-gradient" x1="0" y1="0" x2="0" y2="1">
          <stop offset="0" stop-color="var(--sky-top)"/>
          <stop offset="0.28" stop-color="var(--sky-rose)"/>
          <stop offset="0.45" stop-color="var(--sky-peach)"/>
          <stop offset="0.6" stop-color="var(--sun-gold)"/>
          <stop offset="0.72" stop-color="var(--field-amber)"/>
          <stop offset="1" stop-color="var(--field-dark)"/>
        </linearGradient>
        <radialGradient id="sun-glow" cx="0.48" cy="0.57" r="0.45">
          <stop offset="0" stop-color="var(--sun-core)" stop-opacity="0.95"/>
          <stop offset="0.35" stop-color="var(--sun-gold)" stop-opacity="0.5"/>
          <stop offset="1" stop-color="var(--sun-gold)" stop-opacity="0"/>
        </radialGradient>
      </defs>
      <rect width="1200" height="1200" fill="url(#sky-gradient)"/>
      <rect width="1200" height="1200" fill="url(#sun-glow)"/>
    </svg>

    <p class="cover__label cover__kicker">PODCAST</p>

    <svg class="cover__title" viewBox="0 0 1200 1200" aria-labelledby="show-title">
      <title id="show-title">Beyond the Still</title>
      <text x="600" y="463" font-size="300" text-anchor="middle" textLength="1060" lengthAdjust="spacingAndGlyphs">BEYOND</text>
      <text x="600" y="721" font-size="300" text-anchor="middle">THE</text>
      <text x="600" y="973" font-size="300" text-anchor="middle" textLength="760" lengthAdjust="spacingAndGlyphs">STILL</text>
    </svg>

    <p class="cover__label cover__host">MIRELA DUNFORD</p>
  </main>
</body>
</html>
```